Deckblätter für die Instagram Stories
Zielgruppe
Wir sind ein Handwerksfirma (Maler und Stuckateur Betrieb) und suchen ein hochwertig, frisches, klares Design.
Unsere Zielgruppe sind junge, Männer bzw. im mittleren Alter.
Wir brauchen für unser Instagram (Maler Brunhof) 'Deckblätter' für unsere Stories-Highlights.
Die Themen sind:
-Jobs
-Mitarbeiter
-Azubis
-auf der Baustelle
-News
Aufgabenstellung
Klarheit, Einfachheit

```html
<!DOCTYPE html>
<html lang="de">
<head>
<meta charset="utf-8">
<title>Social Media Design – Meisterbetrieb Brunhof</title>
<link href="https://fonts.googleapis.com/css2?family=Open+Sans:wght@300;400;600;700&family=Permanent+Marker&display=swap" rel="stylesheet">
<style>
  :root{
    --paper:#fbe9d1;
    --orange:#f1a43f;
    --green:#76a834;
    --white:#ffffff;
    --ring:#dfe5e0;
    --ink:#111111;
    --link:#1d3f7a;
    --ig-blue:#3a8ee6;
  }
  *{margin:0;padding:0;box-sizing:border-box}
  html,body{width:1200px;height:847px;overflow:hidden;background:var(--paper)}
  body{position:relative;font-family:"Open Sans",Arial,sans-serif}
  .board-frame{position:absolute;left:0;top:0}
  .board-title{position:absolute;left:46px;top:795px;transform:rotate(-90deg);transform-origin:left top;
    font-weight:700;font-size:18px;color:var(--green);white-space:nowrap;letter-spacing:.1px}
  .highlight{position:absolute;top:48px;width:196px;text-align:center}
  .highlight svg{display:block;margin:0 auto}
  .highlight-label{margin-top:2px;font-weight:300;font-size:19px;line-height:24px;color:var(--green);white-space:nowrap;letter-spacing:.3px}
  .caption{position:absolute;font-weight:600;font-size:13.5px;color:var(--green);white-space:nowrap}

  /* profile screen */
  .profile{position:absolute;left:167px;top:312px;width:197px;height:425px;background:var(--white);border-radius:18px;overflow:hidden;color:var(--ink)}
  .profile-status{display:flex;justify-content:space-between;padding:12px 12px 0 13px;font-size:9.5px;font-weight:600}
  .profile-handle{text-align:center;font-size:7.5px;font-weight:700;margin-top:14px;position:relative}
  .profile-handle span{position:absolute;right:10px;top:-2px;letter-spacing:1px}
  .profile-head{display:flex;align-items:center;margin:10px 0 0 3px}
  .avatar{width:49px;height:49px;border-radius:50%;background:linear-gradient(#c9ced2,#5a6068)}
  .stats{display:flex;flex:1;justify-content:space-around;font-size:7px;text-align:center;line-height:1.25}
  .stats b{font-size:8px;display:block}
  .bio{font-size:6.4px;line-height:1.38;padding:7px 0 0 3px}
  .bio .name{font-weight:700}
  .bio .link{color:var(--link)}
  .bio .more{color:#888}
  .buttons{display:flex;gap:3px;margin:8px 3px 0 3px;font-size:6.5px;font-weight:600}
  .buttons div{height:18px;border-radius:4px;background:#efefef;display:flex;align-items:center;justify-content:center;flex:1}
  .buttons .follow{background:var(--ig-blue);color:var(--white)}
  .buttons .add{flex:0 0 18px}
  .mini-highlights{display:flex;justify-content:space-between;margin:9px 4px 0 4px}
  .tabs{display:flex;justify-content:space-around;margin-top:10px;height:16px;border-bottom:1px solid #ddd}
  .tabs span{width:10px;height:10px;border:1.3px solid #555;border-radius:2px}
  .grid{display:grid;grid-template-columns:repeat(3,1fr);gap:1px;margin-top:0}
  .grid div{height:69px}
  .nav{position:absolute;bottom:0;left:0;right:0;height:52px;background:var(--white);display:flex;justify-content:space-around;padding-top:10px}
  .nav span{width:11px;height:11px;border:1.5px solid #222;border-radius:3px}
  .home-bar{position:absolute;bottom:6px;left:62px;width:73px;height:2px;background:#111;border-radius:2px}

  /* story template */
  .story{position:absolute;left:452px;top:297px;width:265px;height:470px;background:linear-gradient(180deg,#c9d6de 0%,#9b7e63 45%,#7d858a 70%,#3aa7a3 100%)}
  .story-band{position:absolute;left:0;right:0;top:53px;height:74px;background:rgba(255,255,255,.72)}
  .story-title{position:absolute;left:0;right:0;top:66px;text-align:center;font-family:"Permanent Marker",cursive;font-size:44px;line-height:52px;color:var(--orange);letter-spacing:1px}
  .story-badge{position:absolute;left:113px;top:30px}
  .brand-tag{position:absolute;font-weight:400;color:var(--green);white-space:nowrap}
  .story .brand-tag{right:10px;bottom:12px;font-size:13px}

  /* post template */
  .post{position:absolute;left:770px;top:330px;width:342px;height:341px;background:linear-gradient(160deg,#e9e6df 0%,#d1cdc6 50%,#a8835c 100%)}
  .post .brand-tag{right:10px;bottom:10px;font-size:13px}

  .brand-logo{position:absolute;right:14px;top:786px;font-size:26px;line-height:34px;font-weight:400;color:var(--green);letter-spacing:.5px;white-space:nowrap}
</style>
</head>
<body>

<svg width="0" height="0" style="position:absolute" aria-hidden="true">
  <defs>
    <clipPath id="left-half"><rect x="0" y="0" width="96" height="192"/></clipPath>
    <symbol id="badge" viewBox="0 0 192 192">
      <circle cx="96" cy="96" r="94" fill="var(--white)" stroke="var(--ring)" stroke-width="2"/>
      <circle cx="96" cy="100" r="68" fill="var(--orange)"/>
      <circle cx="96" cy="100" r="68" fill="var(--green)" clip-path="url(#left-half)"/>
    </symbol>
    <symbol id="icon-news" viewBox="0 0 100 100">
      <path d="M22 40h14l30-18v56L36 60H22z" fill="var(--white)"/>
      <path d="M38 62l8 20h-9l-8-20z" fill="var(--white)"/>
      <path d="M73 38q8 12 0 24M80 32q13 18 0 36" stroke="var(--white)" stroke-width="4" fill="none" stroke-linecap="round"/>
    </symbol>
    <symbol id="icon-jobs" viewBox="0 0 100 100">
      <path d="M78 20C58 22 42 38 34 58l10 10c20-8 36-24 34-48z" fill="var(--white)"/>
      <circle cx="62" cy="38" r="6" fill="var(--orange)"/>
      <path d="M34 50l-12 4 6-14 14-2zM50 66l-4 12 14-6 2-14z" fill="var(--white)"/>
      <path d="M30 64q-8 4-10 16q12-2 16-10z" fill="var(--white)"/>
    </symbol>
    <symbol id="icon-site" viewBox="0 0 100 100">
      <rect x="28" y="40" width="40" height="42" rx="5" fill="var(--white)"/>
      <ellipse cx="48" cy="40" rx="20" ry="6" fill="var(--white)"/>
      <path d="M28 46q-10 4-4 16" stroke="var(--white)" stroke-width="4" fill="none"/>
      <path d="M56 40l16-20" stroke="var(--white)" stroke-width="6" stroke-linecap="round"/>
      <circle cx="74" cy="18" r="6" fill="var(--white)"/>
    </symbol>
    <symbol id="icon-azubis" viewBox="0 0 100 100">
      <path d="M50 24L92 44 50 62 8 44z" fill="var(--white)"/>
      <path d="M28 52v16q22 10 44 0V52L50 62z" fill="var(--white)"/>
      <path d="M86 47v16" stroke="var(--white)" stroke-width="2.5"/>
      <circle cx="86" cy="65" r="3" fill="var(--white)"/>
    </symbol>
    <symbol id="icon-team" viewBox="0 0 100 100">
      <circle cx="24" cy="40" r="9" fill="var(--white)"/>
      <circle cx="76" cy="40" r="9" fill="var(--white)"/>
      <circle cx="50" cy="36" r="12" fill="var(--white)"/>
      <path d="M8 68q0-18 16-18t16 18z M60 68q0-18 16-18t16 18z" fill="var(--white)"/>
      <path d="M30 70q0-22 20-22t20 22z" fill="var(--white)"/>
    </symbol>
  </defs>
</svg>

<svg class="board-frame" width="1200" height="847" aria-hidden="true">
  <path d="M997 815H55a21 21 0 0 1-21-21V51a21 21 0 0 1 21-21h1090a21 21 0 0 1 21 21v659" fill="none" stroke="var(--orange)" stroke-width="3.5"/>
</svg>

<div class="board-title">Social Media Design Meisterbetrieb Brunhof</div>

<div class="highlight" style="left:77px">
  <svg width="196" height="196" viewBox="0 0 192 192"><use href="#badge"/><use href="#icon-news" x="40" y="44" width="112" height="112"/></svg>
  <div class="highlight-label">NEWS</div>
</div>
<div class="highlight" style="left:294px">
  <svg width="196" height="196" viewBox="0 0 192 192"><use href="#badge"/><use href="#icon-jobs" x="40" y="44" width="112" height="112"/></svg>
  <div class="highlight-label">JOBS</div>
</div>
<div class="highlight" style="left:506px">
  <svg width="196" height="196" viewBox="0 0 192 192"><use href="#badge"/><use href="#icon-site" x="40" y="44" width="112" height="112"/></svg>
  <div class="highlight-label">AUF DER BAUSTELLE</div>
</div>
<div class="highlight" style="left:719px">
  <svg width="196" height="196" viewBox="0 0 192 192"><use href="#badge"/><use href="#icon-azubis" x="40" y="44" width="112" height="112"/></svg>
  <div class="highlight-label">AZUBIS</div>
</div>
<div class="highlight" style="left:931px">
  <svg width="196" height="196" viewBox="0 0 192 192"><use href="#badge"/><use href="#icon-team" x="40" y="44" width="112" height="112"/></svg>
  <div class="highlight-label">MITARBEITER</div>
</div>

<section class="profile">
  <div class="profile-status"><span>14:44</span><span>▮▮▮</span></div>
  <div class="profile-handle">malerbrunhof<span>···</span></div>
  <div class="profile-head">
    <div class="avatar" role="img" aria-label="Profilfoto: drei Männer des Betriebs"></div>
    <div class="stats">
      <div><b>48</b>Beiträge</div>
      <div><b>333</b>Follower</div>
      <div><b>190</b>Gefolgt</div>
    </div>
  </div>
  <div class="bio">
    <div class="name">Meisterbetrieb Maler Brunhof</div>
    <div class="link">Produkt/Dienstleistung</div>
    <div>Familienbetrieb in dritter Generation seit 1971 ⚒</div>
    <div>Innen - Außen</div>
    <div>Erhalten - Gestalten… <span class="more">mehr</span></div>
    <div class="link">maler-brunhof.de/</div>
    <div class="link">Lindenweg 12, Talheim</div>
  </div>
  <div class="buttons">
    <div class="follow">Folgen</div><div>Nachricht</div><div>Kontakt</div><div class="add">+</div>
  </div>
  <div class="mini-highlights">
    <svg width="33" height="33" viewBox="0 0 192 192"><use href="#badge"/><use href="#icon-news" x="40" y="44" width="112" height="112"/></svg>
    <svg width="33" height="33" viewBox="0 0 192 192"><use href="#badge"/><use href="#icon-jobs" x="40" y="44" width="112" height="112"/></svg>
    <svg width="33" height="33" viewBox="0 0 192 192"><use href="#badge"/><use href="#icon-site" x="40" y="44" width="112" height="112"/></svg>
    <svg width="33" height="33" viewBox="0 0 192 192"><use href="#badge"/><use href="#icon-azubis" x="40" y="44" width="112" height="112"/></svg>
    <svg width="33" height="33" viewBox="0 0 192 192"><use href="#badge"/><use href="#icon-team" x="40" y="44" width="112" height="112"/></svg>
  </div>
  <div class="tabs"><span></span><span></span><span></span></div>
  <div class="grid">
    <div role="img" aria-label="Foto: Treppenhaus mit Holzboden" style="background:linear-gradient(#d9d6d0,#9a7b55)"></div>
    <div role="img" aria-label="Foto: Handwerker beim Verputzen" style="background:linear-gradient(#bfc2c0,#6f7370)"></div>
    <div role="img" aria-label="Foto: eingerüstetes Gebäude" style="background:linear-gradient(#8fb0d6,#5d7a55)"></div>
    <div role="img" aria-label="Foto: Wand mit gelbem Bild" style="background:linear-gradient(#f0eeea,#d9c36a)"></div>
    <div role="img" aria-label="Foto: Innenraum mit Fenster" style="background:linear-gradient(#d7b48a,#8a6a50)"></div>
    <div role="img" aria-label="Foto: Altbaufassade" style="background:linear-gradient(#9aa0a3,#e4e2dc)"></div>
  </div>
  <div class="nav"><span></span><span></span><span></span><span></span><span></span></div>
  <div class="home-bar"></div>
</section>
<div class="caption" style="left:158px;top:756px">Beispiel - Highlightbuttons</div>

<section class="story" role="img" aria-label="Story-Vorlage: Malermeister schleift einen türkisen Fensterladen vor Paletten und Gerüst">
  <div class="story-band"></div>
  <svg class="story-badge" width="40" height="40" viewBox="0 0 192 192"><circle cx="96" cy="100" r="68" fill="var(--orange)"/><circle cx="96" cy="100" r="68" fill="var(--green)" clip-path="url(#left-half)"/><use href="#icon-news" x="40" y="44" width="112" height="112"/></svg>
  <div class="story-title">NEWS</div>
  <div class="brand-tag">maler Brunhof</div>
</section>
<div class="caption" style="left:452px;top:773px">Designvorlage - Instagram-Story</div>

<section class="post" role="img" aria-label="Post-Vorlage: offener Wohnraum mit grauem Spachtelboden, Küche und Holzparkett">
  <div class="brand-tag">maler Brunhof</div>
</section>
<div class="caption" style="left:770px;top:679px">Designvorlage - Instagram-Post</div>

<div class="brand-logo">maler Brunhof</div>

</body>
</html>
```